Luxury Courtside Grove/academy - Webdesign

We want to develop a cutting edge website for a luxury tennis academy. Academy is based in Russia and includes all the necessary amenities for comfortable stay: apartments, spa, tennis courts, training facilities, etc.
We would like to see a clean, simple and modern design (with implementation of all the current trends in web design, although our project has to be distinct and unique).
Color scheme: we would like to see colors present in our logos and all the current associated with tennis. We are open to your ideas and creativity on this front.
The final design should communicate simplicity, be user friendly and convey premium feel.
We woud like to see unique ideas in the design, unconventional techniques, etc.
We don't want standard template design!
Updates
We want to mention that this Tennis Academy has a light focus on nature, as the new material we have uploaded illustrates.
Additional comment to everyone!
We couldn't upload this file to the system: it is too big.
Thank you everyone for your submissions!
Industry/Entity Type
Training
Requirements
Must have
- We would like to see the designs for the following pages:
Home Page:
- Slideshow
- Short description and all the standard stuff
About Us:
- Description with some images
Services:
- Simple description of all of the provided services and possibility to book all of them on the website
! Important ! Develop small system for booking of the days of stay and registration for the courses
Booking and registration !
News:
- Creative layout to display recent news of the academy
Coaches:
- Image and short description of our staff.
Club / Gallery:
- Images and descriptions of the amenities in the territory.
We want a unique display of images: not just lines and rows filled with images
- One idea: an interactive map that displays images and description on mouseover or click on the object on the map (but again, we are open to all your ideas)
Contacts:
- Contact form, contacts, etc.
Sport Store:
- Basic layout for the goods and services provided by the sports store located in the academy
Prices:
- Price lists and ranges with a button leading to registration and booking
For pages like About Us and Services, it would be enough to develop one unified layout for all of them.

```html
<!DOCTYPE html>
<html lang="fr">
<head>
<meta charset="utf-8">
<title>Courtside Grove</title>
<link href="https://fonts.googleapis.com/css2?family=Ubuntu:wght@400;500;700&family=Yanone+Kaffeesatz:wght@300;400&family=Arimo:wght@400&display=swap" rel="stylesheet">
<style>
:root{
  --green:#4a8c24;
  --green-dark:#2f6b14;
  --green-light:#6cbf3a;
  --ink:#3d3d3d;
  --body-text:#1f4a4a;
  --muted:#6a6a6a;
  --page:#f7f7f7;
  --rule:#e3e3e3;
  --white:#ffffff;
}
*{margin:0;padding:0;box-sizing:border-box}
html,body{width:1200px;height:1111px;overflow:hidden}
body{position:relative;background:var(--page);font-family:"Ubuntu",sans-serif;color:var(--ink)}
.hero-photo{position:absolute;left:0;top:0;width:1200px;height:546px;
  background:linear-gradient(180deg,#c9dcec 0%,#e4e9ea 22%,#d9d6cc 40%,#a27257 58%,#8a5a3f 70%,#5f6b3a 80%,#4a7a28 90%,#3d6a1f 100%)}
.header{position:absolute;left:0;top:0;width:1200px;height:100px;
  background:linear-gradient(180deg,rgba(255,255,255,.92),rgba(255,255,255,.78));
  box-shadow:0 2px 6px rgba(0,0,0,.12)}
.brand{position:absolute;left:182px;top:30px;display:flex;align-items:center;gap:8px;
  font-family:"Ubuntu",sans-serif;font-weight:700;font-size:26px;color:var(--green-dark)}
.brand-dot{width:18px;height:18px;border-radius:50%;background:var(--green-light)}
.search{position:absolute;left:866px;top:21px;width:154px;height:19px;border:1px solid #d8d8d8;border-radius:10px;
  background:#fbfbfb;font-family:"Arimo",sans-serif;font-style:italic;font-size:8.5px;color:#9a9a9a;padding:4px 11px}
.nav{position:absolute;top:62px;left:0;width:1200px;height:25px;list-style:none}
.nav li{position:absolute;top:0;height:25px;line-height:25px;transform:translateX(-50%);
  font-family:"Yanone Kaffeesatz",sans-serif;font-weight:300;font-size:16px;color:#3a3a3a;white-space:nowrap}
.nav li.active{background:linear-gradient(#69b23a,#3f8a1c);color:var(--white);border:1px solid #3a7a1a;border-radius:3px;padding:0 8px;font-weight:400}
.hero-title{position:absolute;left:183px;top:216px;font-family:"Arimo",sans-serif;font-size:32px;line-height:40px;color:#111;letter-spacing:-.5px}
.hero-text{position:absolute;left:184px;top:315px;width:420px;font-family:"Arimo",sans-serif;font-size:12px;line-height:20.5px;color:var(--white)}
.btn{position:absolute;display:flex;align-items:center;justify-content:center;font-family:"Arimo",sans-serif;color:#222;
  background:linear-gradient(#ffffff,#e4e4e4);border:1px solid #cfcfcf;border-radius:4px;box-shadow:0 1px 3px rgba(0,0,0,.25)}
.btn-hero{left:184px;top:403px;width:173px;height:44px;font-size:20px;border-radius:8px}
.dots{position:absolute;left:567px;top:515px;display:flex;gap:7px}
.dots span{width:11px;height:11px;border-radius:50%;background:rgba(220,220,220,.8)}
.dots span.on{background:var(--green-light)}
.join{position:absolute;left:0;top:546px;width:1200px;height:79px;background:var(--green);
  border-top:2px solid #3b7a1a;border-bottom:2px solid #2c6210}
.join-title{position:absolute;left:184px;top:18px;font-family:"Arimo",sans-serif;font-size:36px;color:var(--white);letter-spacing:-.5px}
.join-divider{position:absolute;left:511px;top:6px;width:1px;height:66px;background:rgba(0,0,0,.18);box-shadow:1px 0 0 rgba(255,255,255,.15)}
.join-text{position:absolute;left:531px;top:16px;width:345px;font-family:"Arimo",sans-serif;font-size:11px;line-height:16.5px;color:var(--white)}
.btn-join{left:895px;top:15px;width:125px;height:46px;font-size:18px;border-radius:2px}
.service{position:absolute;width:250px}
.service h3{position:absolute;left:50px;top:0;font-size:20px;font-weight:500;color:var(--ink)}
.service p{position:absolute;left:50px;top:26px;width:200px;font-size:10.3px;line-height:16.3px;color:var(--body-text)}
.service svg{position:absolute;left:0;top:33px}
.rule{position:absolute;left:182px;width:838px;height:1px;background:var(--rule)}
.welcome h2{position:absolute;left:183px;top:937px;font-size:19px;font-weight:500;color:var(--ink)}
.welcome p{position:absolute;left:183px;top:975px;width:830px;font-size:10.9px;line-height:13.8px;color:#333}
.footer-nav{position:absolute;left:186px;top:1075px;font-size:9.5px;color:var(--muted)}
.footer-nav span{margin:0 4px;color:#aaa}
.copyright{position:absolute;right:188px;top:1075px;font-size:9.5px;color:var(--muted)}
</style>
</head>
<body>
<div class="hero-photo" role="img" aria-label="Photo of outdoor clay tennis courts with players, an inflatable dome and club houses under a cloudy sky, grass in the foreground"></div>

<header class="header">
  <div class="brand"><span>Courtside Grove</span><span class="brand-dot"></span></div>
  <div class="search">Enter Your Search</div>
  <ul class="nav">
    <li class="active" style="left:417px">HOME</li>
    <li style="left:489px">ABOUT US</li>
    <li style="left:561px">SERVICES</li>
    <li style="left:634px">NEWS</li>
    <li style="left:707px">COACHES</li>
    <li style="left:779px">GALLERY</li>
    <li style="left:853px">CONTACTS</li>
    <li style="left:926px">SPORT STORE</li>
    <li style="left:999px">PRICES</li>
  </ul>
</header>

<h1 class="hero-title">Contrairementaune opinion<br>répandue le Lorem Ipsum nest.</h1>
<p class="hero-text">Le Lorem Ipsum est simplement du faux texte employé dans la composition et la mise en page avant impression. Le Lorem Ipsum est le faux texte standard de l'imprimerie depuis les années 1500,</p>
<a class="btn btn-hero">Know More</a>
<div class="dots"><span class="on"></span><span></span><span></span><span></span></div>

<section class="join">
  <h2 class="join-title">WANT TO JOIN US?</h2>
  <div class="join-divider"></div>
  <p class="join-text">Le Lorem Ipsum est simplement du faux texte employé dans la com-position et la mise en page avant impression. Le Lorem Ipsum est le faux texte standard de l'imprimerie depuis les années 1500.</p>
  <a class="btn btn-join">Read More</a>
</section>

<svg width="0" height="0" style="position:absolute">
  <defs>
    <radialGradient id="badge" cx="40%" cy="30%" r="75%">
      <stop offset="0" stop-color="#7cc84a"/><stop offset="1" stop-color="#2f7a14"/>
    </radialGradient>
  </defs>
</svg>

<div class="service" style="left:181px;top:662px">
  <h3>TENNIS</h3>
  <svg width="45" height="45" viewBox="0 0 45 45"><circle cx="22.5" cy="22.5" r="22" fill="url(#badge)"/><circle cx="22.5" cy="22.5" r="10" fill="#fff"/><path d="M14 17c5 2 7 7 5 13M31 15c-5 2-7 8-4 13" stroke="#3f8a1c" stroke-width="1.5" fill="none"/></svg>
  <p>Le Lorem Ipsum est simplement du faux texte employé dans la composition et la mise en page avant impression.</p>
</div>
<div class="service" style="left:483px;top:662px">
  <h3>SPA</h3>
  <svg width="45" height="45" viewBox="0 0 45 45"><circle cx="22.5" cy="22.5" r="22" fill="url(#badge)"/><ellipse cx="21" cy="15" rx="5" ry="2.5" fill="#fff"/><ellipse cx="21" cy="21" rx="8" ry="3" fill="#fff"/><ellipse cx="21" cy="28" rx="11" ry="3.5" fill="#fff"/></svg>
  <p>Le Lorem Ipsum est simplement du faux texte employé dans la composition et la mise en page avant impression.</p>
</div>
<div class="service" style="left:786px;top:662px">
  <h3>BEAUTY CENTER</h3>
  <svg width="45" height="45" viewBox="0 0 45 45"><circle cx="22.5" cy="22.5" r="22" fill="url(#badge)"/><circle cx="22.5" cy="22.5" r="4" fill="#fff"/><g fill="#fff"><circle cx="22.5" cy="14" r="4"/><circle cx="22.5" cy="31" r="4"/><circle cx="14" cy="22.5" r="4"/><circle cx="31" cy="22.5" r="4"/></g><circle cx="22.5" cy="22.5" r="3" fill="#3f8a1c"/></svg>
  <p>Le Lorem Ipsum est simplement du faux texte employé dans la composition et la mise en page avant impression.</p>
</div>

<div class="service" style="left:181px;top:785px">
  <h3>FOREST</h3>
  <svg width="45" height="45" viewBox="0 0 45 45"><circle cx="22.5" cy="22.5" r="22" fill="url(#badge)"/><circle cx="22.5" cy="18" r="9" fill="#fff"/><rect x="21" y="24" width="3" height="10" fill="#fff"/></svg>
  <p>Le Lorem Ipsum est simplement du faux texte employé dans la composition et la mise en page avant impression.</p>
</div>
<div class="service" style="left:483px;top:785px">
  <h3>HORSE RIDING</h3>
  <svg width="45" height="45" viewBox="0 0 45 45"><circle cx="22.5" cy="22.5" r="22" fill="url(#badge)"/><path d="M15 31V21a7.5 7.5 0 0 1 15 0v10" stroke="#fff" stroke-width="4" fill="none" stroke-linecap="round"/></svg>
  <p>Le Lorem Ipsum est simplement du faux texte employé dans la composition et la mise en page avant impression.</p>
</div>
<div class="service" style="left:786px;top:785px">
  <h3>TRAINING</h3>
  <svg width="45" height="45" viewBox="0 0 45 45"><circle cx="22.5" cy="22.5" r="22" fill="url(#badge)"/><circle cx="22.5" cy="24" r="9" stroke="#fff" stroke-width="2.5" fill="none"/><rect x="20.5" y="11" width="4" height="3" fill="#fff"/><path d="M22.5 24v-5" stroke="#fff" stroke-width="2" stroke-linecap="round"/></svg>
  <p>Le Lorem Ipsum est simplement du faux texte employé dans la composition et la mise en page avant impression.</p>
</div>

<div class="rule" style="top:909px"></div>
<section class="welcome">
  <h2>WELCOME TO COURTSIDE GROVE</h2>
  <p>Le Lorem Ipsum est simplement du faux texte employé dans la composition et la mise en page avant impression. Le Lorem Ipsum est le faux texte standard de l'imprimerie depuis les années 1500, quand un peintre anonyme Le Lorem Ipsum est simplemen.t du faux texte employé dans la composition et la mise en page avant impression. Le Lorem Ipsum est le faux texte standard.</p>
</section>
<div class="rule" style="top:1051px"></div>

<footer>
  <nav class="footer-nav">Home<span>|</span>About Us<span>|</span>Services<span>|</span>News<span>|</span>Coaches<span>|</span>Gallery<span>|</span>Contacts<span>|</span>Sport Store<span>|</span>Prices</nav>
  <div class="copyright">© Copyrights 2012 All rights Reserved</div>
</footer>
</body>
</html>
```